Wine Bottle Label

We would like a custom label for a wine bottle. We are a retailer of locally produced wines in a tourist town with a rich Dutch heritage. Our store is called The Vat Cellar (wijn is Dutch for wine). We would like something that says "Vat Cellar Red" and has a really classy look to it. We would also like to incorporate the "tulip bottle" in our logo which many customers recognize us by. Other traditional Dutch items like a windmill or a clog are optional. the design must incorporate the words "Pella, Iowa" somewhere as the tourist traffic always wants a "bottle that says Pella on it". Our customers are largely female and tend to be fans of the "buy local, drink local" crowd. We want something classic, but not pretentious. In my mind the background is dark or black, but will look at other options as well, will likely be on a black-glass bottle. If the color scheme could be changed very simply later to allow for a "Vat Cellar White" option that would be even better.

```html
<!DOCTYPE html>
<html lang="en">
<head>
<meta charset="utf-8">
<title>Vat Cellar White — Wine Label</title>
<link rel="stylesheet" href="https://fonts.googleapis.com/css2?family=Tinos&family=Mrs+Saint+Delafield&display=swap">
<style>
  :root {
    --backdrop: #f2f1ef;
    --label-paper: #fdfdfc;
    --ink: #1c1a1a;
    --burgundy: #7a2533;
    --petal-light: #f3dadd;
    --petal-mid: #d99aa3;
    --stem-mauve: #b58d95;
  }
  * { margin: 0; padding: 0; box-sizing: border-box; }
  html, body {
    width: 1200px;
    height: 1200px;
    overflow: hidden;
    background: var(--backdrop);
  }
  .canvas {
    position: relative;
    width: 1200px;
    height: 1200px;
  }
  .wine-label {
    position: absolute;
    left: 250px;
    top: 140px;
    width: 700px;
    height: 920px;
    background: var(--label-paper);
    box-shadow: 0 2px 14px rgba(0, 0, 0, 0.08);
    overflow: hidden;
  }
  .tulip-artwork {
    position: absolute;
    left: 20px;
    top: 90px;
    width: 360px;
    height: 830px;
  }
  .store-name {
    position: absolute;
    left: 400px;
    top: 215px;
    width: 280px;
    text-align: center;
    font-family: "Tinos", "Times New Roman", serif;
    font-size: 34px;
    color: var(--burgundy);
    letter-spacing: 0.02em;
  }
  .wine-title {
    position: absolute;
    left: 360px;
    top: 470px;
    width: 320px;
    text-align: center;
    font-family: "Tinos", "Times New Roman", serif;
    font-weight: 400;
    font-size: 60px;
    line-height: 1;
    color: var(--ink);
  }
  .wine-style {
    position: absolute;
    left: 350px;
    top: 548px;
    width: 340px;
    text-align: center;
    font-family: "Mrs Saint Delafield", cursive;
    font-size: 118px;
    line-height: 1;
    color: var(--ink);
  }
  .origin {
    position: absolute;
    left: 360px;
    top: 805px;
    width: 310px;
    text-align: center;
    font-family: "Tinos", "Times New Roman", serif;
    font-size: 28px;
    letter-spacing: 0.22em;
    color: var(--ink);
  }
  .bottle-details {
    position: absolute;
    left: 350px;
    top: 868px;
    width: 330px;
    text-align: center;
    font-family: "Tinos", "Times New Roman", serif;
    font-size: 20px;
    color: var(--ink);
  }
</style>
</head>
<body>
<main class="canvas">
  <section class="wine-label">
    <svg class="tulip-artwork" viewBox="0 0 360 830" role="img" aria-label="Illustration of pink tulips on curling stems with a small butterfly and dotted flight path">
      <defs>
        <linearGradient id="tulipFieldTone" x1="0" y1="0" x2="0.3" y2="1">
          <stop offset="0" stop-color="var(--petal-mid)" stop-opacity="0.55"/>
          <stop offset="0.5" stop-color="var(--petal-light)" stop-opacity="0.6"/>
          <stop offset="1" stop-color="var(--stem-mauve)" stop-opacity="0.45"/>
        </linearGradient>
      </defs>
      <rect width="360" height="830" fill="url(#tulipFieldTone)"/>
    </svg>

    <p class="store-name">The Vat Cellar</p>

    <h1 class="wine-title">Vat Cellar</h1>
    <p class="wine-style">White</p>

    <p class="origin">PELLA, IOWA</p>
    <p class="bottle-details">750mL XX% abv Grape Varietal</p>
  </section>
</main>
</body>
</html>
```